New Business Card Design Project VORASTI-Italy

we are VORASTI-Italy
our company in the market for 3 years we are luxury cosmetic company and its about time for a facelift :)
i will like to have elegant luxurious and unique business card
that will give the person that get it a unique, luxurious and elegant impression
I'm VERY OPEN FOR NEW IDEAS , even duo i add a few files of things that i see on line and i like them

i add my logo as well
my website is VORASTI.COM
(if you would like to see the main style that we have)

Target Market(s)

adult that have money :)

Industry/Entity Type

Business

Contact Information for Business Card

Name - Paul Vorasti
Position - CEO and CO Founder
address - 4817 E Larkdale
telephone - 555-384-1962
email - paul@vorasti.com
fax - 555-384-1962
website - VORASTI.COM

Colors
000000
959595
fbee3e
ffffff

Requirements
Must have
• big logo in GOLD color
• elegant look
• impressive
Nice to have
• not must but maybe classy pattern background
• not must but maybe emblem
• maybe clear plastic business card
Should not have
• colors
• images

```html
<!DOCTYPE html>
<html lang="en">
<head>
<meta charset="utf-8">
<title>VORASTI Italy – Business Card</title>
<link rel="stylesheet" href="https://fonts.googleapis.com/css2?family=EB+Garamond:wght@500&family=Open+Sans:wght@400;600;700&display=swap">
<style>
  :root {
    --backdrop: #2a2725;
    --card: #0e0e0e;
    --card-edge: #1a1a1a;
    --gold: #d9ae3c;
    --gold-deep: #b8891f;
    --white: #ffffff;
    --grey: #959595;
    --faint: #262626;
  }
  * { margin: 0; padding: 0; box-sizing: border-box; }
  html, body { width: 1200px; height: 716px; overflow: hidden; }
  body {
    background: var(--backdrop);
    position: relative;
    font-family: "Open Sans", Arial, sans-serif;
  }
  .card {
    position: absolute;
    top: 208px;
    width: 520px;
    height: 300px;
    background: var(--card);
    border: 1px solid var(--card-edge);
    box-shadow: 0 18px 40px rgba(0,0,0,.55);
    overflow: hidden;
  }
  .card--front { left: 50px; }
  .card--back { left: 630px; }

  /* Front */
  .front-lockup {
    position: absolute;
    left: 0; right: 0; top: 46px;
    display: flex; flex-direction: column; align-items: center;
  }
  .brand-dot {
    width: 74px; height: 74px;
    border: 3px solid var(--gold);
    border-radius: 50%;
    margin-bottom: 14px;
  }
  .brand-name {
    font-family: "EB Garamond", Georgia, serif;
    font-weight: 500;
    color: var(--gold);
    letter-spacing: 1px;
    line-height: 1;
  }
  .front-lockup .brand-name { font-size: 56px; }
  .brand-rule { height: 2px; background: var(--gold); }
  .front-lockup .brand-rule { width: 250px; margin: 8px 0 6px; }
  .brand-region {
    font-family: "EB Garamond", Georgia, serif;
    font-weight: 500;
    color: var(--gold);
    letter-spacing: 2px;
  }
  .front-lockup .brand-region { font-size: 17px; }

  /* Back */
  .back-lockup {
    position: absolute;
    left: 150px; top: 24px; width: 150px;
    display: flex; flex-direction: column; align-items: center;
  }
  .back-lockup .brand-dot { width: 38px; height: 38px; border-width: 2px; margin-bottom: 8px; }
  .back-lockup .brand-name { font-size: 29px; }
  .back-lockup .brand-rule { width: 140px; margin: 3px 0 2px; height: 1px; }
  .back-lockup .brand-region { font-size: 10px; }

  .holder { position: absolute; left: 70px; top: 128px; }
  .holder-name { color: var(--white); font-weight: 700; font-size: 15px; }
  .holder-role { color: var(--grey); font-size: 7px; margin-top: 1px; }
  .holder-rule {
    position: absolute; left: 70px; top: 164px;
    width: 230px; height: 1px; background: var(--gold);
  }

  .contacts { position: absolute; left: 50px; top: 178px; list-style: none; }
  .contact {
    display: flex; align-items: center; gap: 10px;
    color: var(--white); font-weight: 600; font-size: 12px;
    height: 17px;
  }
  .contact svg { width: 11px; height: 11px; fill: var(--gold); flex: none; }
  .contact--indent { padding-left: 21px; }

  .seal-faint {
    position: absolute; left: 320px; top: 60px;
    width: 190px; height: 190px;
    border: 6px solid var(--faint);
    border-radius: 50%;
  }

  .edge-band {
    position: absolute; left: 0; bottom: 24px;
    width: 356px; height: 3px; background: var(--gold);
  }
  .address-tab {
    position: absolute; right: 0; bottom: 0;
    width: 190px; height: 27px;
    background: var(--gold);
    clip-path: polygon(10px 0, 100% 0, 100% 100%, 0 100%, 0 3px);
    display: flex; align-items: center; gap: 10px;
    padding-left: 24px;
    color: #111; font-weight: 700; font-size: 13px;
  }
  .address-tab svg { width: 10px; height: 13px; fill: #111; }
  .bottom-line {
    position: absolute; left: 0; bottom: 0; width: 330px; height: 24px;
  }
</style>
</head>
<body>
  <section class="card card--front" aria-label="Card front">
    <div class="front-lockup">
      <span class="brand-dot"></span>
      <span class="brand-name">VORASTI</span>
      <span class="brand-rule"></span>
      <span class="brand-region">ITALY</span>
    </div>
  </section>

  <section class="card card--back" aria-label="Card back">
    <div class="seal-faint" aria-hidden="true"></div>

    <div class="back-lockup">
      <span class="brand-dot"></span>
      <span class="brand-name">VORASTI</span>
      <span class="brand-rule"></span>
      <span class="brand-region">ITALY</span>
    </div>

    <div class="holder">
      <p class="holder-name">Paul Vorasti</p>
      <p class="holder-role">Position - CEO and CO Founder</p>
    </div>
    <div class="holder-rule"></div>

    <ul class="contacts">
      <li class="contact contact--indent">
        <svg viewBox="0 0 24 24"><path d="M6.6 10.8a15.1 15.1 0 0 0 6.6 6.6l2.2-2.2c.3-.3.7-.4 1-.2 1.1.4 2.3.6 3.6.6.6 0 1 .4 1 1V20c0 .6-.4 1-1 1A17 17 0 0 1 3 4c0-.6.4-1 1-1h3.5c.6 0 1 .4 1 1 0 1.3.2 2.5.6 3.6.1.3 0 .7-.2 1z"/></svg>
        555-384-1962
      </li>
      <li class="contact contact--indent">
        <svg viewBox="0 0 24 24"><path d="M2 5h20v14H2zm2 2v.5l8 5 8-5V7zm0 2.8V17h16V9.8l-8 5z"/></svg>
        paul@vorasti.com
      </li>
      <li class="contact">
        <svg viewBox="0 0 24 24"><path d="M6 2h9l3 3v5h2a2 2 0 0 1 2 2v8a2 2 0 0 1-2 2H4a2 2 0 0 1-2-2v-8a2 2 0 0 1 2-2h2zm2 2v6h8V6h-2V4zm8 10v2h2v-2zm-4 0v2h2v-2z"/></svg>
        555-384-1962
      </li>
      <li class="contact">
        <svg viewBox="0 0 24 24"><path d="M12 2a10 10 0 1 0 0 20 10 10 0 0 0 0-20zm6.9 9h-3a15 15 0 0 0-1.3-5.6A8 8 0 0 1 18.9 11zM12 4c.9 1.2 1.8 3.7 1.9 7h-3.8C10.2 7.7 11.1 5.2 12 4zM9.4 5.4A15 15 0 0 0 8.1 11h-3a8 8 0 0 1 4.3-5.6zM5.1 13h3a15 15 0 0 0 1.3 5.6A8 8 0 0 1 5.1 13zM12 20c-.9-1.2-1.8-3.7-1.9-7h3.8c-.1 3.3-1 5.8-1.9 7zm2.6-1.4a15 15 0 0 0 1.3-5.6h3a8 8 0 0 1-4.3 5.6z"/></svg>
        VORASTI.COM
      </li>
    </ul>

    <div class="edge-band"></div>
    <div class="address-tab">
      <svg viewBox="0 0 20 26"><path d="M10 0a10 10 0 0 0-10 10c0 7.5 10 16 10 16s10-8.5 10-16A10 10 0 0 0 10 0zm0 14a4 4 0 1 1 0-8 4 4 0 0 1 0 8z"/></svg>
      4817 E Larkdale
    </div>
  </section>
</body>
</html>
```